VELMARA IMAGING
Ultrasound Imaging Services
VELMARA IMAGING - Imaging
Creative Brief
Professional
Dorvan Tessliff
Ultrasound Diagnostic
5873 Calloway ridge ln Raleigh, NC 27614
dorvantessliff@mailvane.net
Concepts
Logo for mobile ultrasound

```html
<!DOCTYPE html>
<html lang="en">
<head>
<meta charset="utf-8">
<title>Velmara Imaging – Business Card</title>
<link rel="stylesheet" href="https://fonts.googleapis.com/css2?family=Montserrat:wght@400;500;600;800&display=swap">
<style>
  :root {
    --bg: #e9e8ee;
    --card: #ffffff;
    --navy: #2a2886;
    --navy-deep: #1d1b6b;
    --lilac: #bcb8e8;
    --lilac-soft: #dcdaf3;
    --cyan: #35b3d6;
    --ink: #2c2c3a;
    --muted: #6c6c80;
  }
  * { box-sizing: border-box; margin: 0; padding: 0; }
  html, body { width: 1200px; height: 828px; overflow: hidden; }
  body {
    background: var(--bg);
    font-family: "Montserrat", Arial, sans-serif;
    position: relative;
  }
  .card {
    position: absolute;
    top: 266px;
    width: 520px;
    height: 297px;
    background: var(--card);
    box-shadow: 0 6px 20px rgba(40, 40, 80, 0.15);
    overflow: hidden;
  }
  .card--front { left: 60px; }
  .card--back { left: 620px; }
  .card__art { position: absolute; inset: 0; width: 100%; height: 100%; }

  .brand { position: absolute; display: flex; flex-direction: column; }
  .brand__row { display: flex; align-items: center; gap: 8px; }
  .brand__dot { width: 14px; height: 14px; border-radius: 50%; background: var(--cyan); }
  .brand__name {
    font-weight: 800;
    font-size: 34px;
    letter-spacing: 1px;
    color: var(--navy);
    line-height: 1;
  }
  .brand__service {
    font-weight: 600;
    font-size: 10.5px;
    letter-spacing: 0.6px;
    color: var(--navy);
    margin-top: 4px;
    margin-left: 22px;
    text-transform: uppercase;
  }
  .brand__motto {
    font-size: 8px;
    color: var(--cyan);
    margin-top: 3px;
    margin-left: 22px;
  }
  .card--front .brand { left: 40px; top: 150px; }
  .card--back .brand { left: 300px; top: 208px; }
  .card--back .brand__name { font-size: 28px; }

  .person { position: absolute; right: 28px; top: 30px; text-align: right; }
  .person__name { font-size: 17px; font-weight: 600; color: var(--navy); letter-spacing: 1px; text-transform: uppercase; }
  .person__role { font-size: 8px; color: var(--muted); letter-spacing: 1.5px; margin-top: 2px; }

  .contact { position: absolute; right: 28px; top: 84px; list-style: none; text-align: right; }
  .contact li {
    font-size: 8.5px;
    color: var(--ink);
    line-height: 15px;
    display: flex;
    justify-content: flex-end;
    align-items: center;
    gap: 6px;
  }
  .contact svg { width: 9px; height: 9px; fill: var(--navy); }
  .contact .contact__gap { height: 6px; }
</style>
</head>
<body>
  <section class="card card--front" aria-label="Card front">
    <svg class="card__art" viewBox="0 0 520 297" preserveAspectRatio="none" aria-hidden="true">
      <path d="M250 0 C330 40 380 80 520 70 L520 0 Z" fill="var(--lilac-soft)"/>
      <path d="M270 0 C350 30 420 58 520 50 L520 40 C430 44 360 25 300 0 Z" fill="var(--lilac)"/>
      <path d="M330 0 C400 22 460 34 520 30 L520 14 C470 18 420 10 380 0 Z" fill="var(--navy)"/>
      <path d="M260 0 C340 60 420 110 520 120 L520 112 C430 100 350 55 285 0 Z" fill="var(--lilac)" opacity="0.7"/>
    </svg>
    <div class="brand">
      <div class="brand__row"><span class="brand__dot"></span><span class="brand__name">VELMARA</span></div>
      <span class="brand__service">Imaging Ultrasound Services</span>
      <span class="brand__motto">Mobile care you trust</span>
    </div>
  </section>

  <section class="card card--back" aria-label="Card back">
    <svg class="card__art" viewBox="0 0 520 297" preserveAspectRatio="none" aria-hidden="true">
      <path d="M0 0 L210 0 C150 80 200 200 290 297 L0 297 Z" fill="var(--navy)"/>
      <path d="M210 0 C150 80 200 200 290 297 L276 297 C186 200 136 90 196 0 Z" fill="var(--navy-deep)"/>
      <path d="M222 0 C168 80 214 200 306 297 L292 297 C200 200 154 80 212 0 Z" fill="var(--lilac)"/>
      <path d="M236 0 C186 90 236 210 330 297 L318 297 C222 210 176 90 228 0 Z" fill="var(--lilac-soft)"/>
    </svg>
    <div class="person">
      <p class="person__name">Dorvan Tessliff</p>
      <p class="person__role">DIRECTOR</p>
    </div>
    <ul class="contact">
      <li>5873 Calloway ridge ln</li>
      <li>Raleigh, NC 27614
        <svg viewBox="0 0 10 10"><path d="M5 0a3.5 3.5 0 0 0-3.5 3.5C1.5 6 5 10 5 10s3.5-4 3.5-6.5A3.5 3.5 0 0 0 5 0zm0 5a1.5 1.5 0 1 1 0-3 1.5 1.5 0 0 1 0 3z"/></svg></li>
      <li class="contact__gap"></li>
      <li>919 555 0142
        <svg viewBox="0 0 10 10"><path d="M2 0l2 2.5-1 1.2a6 6 0 0 0 3.3 3.3l1.2-1L10 8 8.5 10C4 10 0 6 0 1.5z"/></svg></li>
      <li>919 555 0187
        <svg viewBox="0 0 10 10"><path d="M2 0l2 2.5-1 1.2a6 6 0 0 0 3.3 3.3l1.2-1L10 8 8.5 10C4 10 0 6 0 1.5z"/></svg></li>
      <li>919 555 0163
        <svg viewBox="0 0 10 10"><rect x="1" y="0" width="8" height="10" rx="1"/></svg></li>
      <li class="contact__gap"></li>
      <li>dorvantessliff@mailvane.net
        <svg viewBox="0 0 10 10"><path d="M0 2h10v6H0z M0 2l5 3.5L10 2" /></svg></li>
      <li>www.velmaraimaging.net</li>
    </ul>
    <div class="brand">
      <div class="brand__row"><span class="brand__dot"></span><span class="brand__name">VELMARA</span></div>
      <span class="brand__service">Imaging Ultrasound Services</span>
      <span class="brand__motto">Mobile care you trust</span>
    </div>
  </section>
</body>
</html>
```